Business card design needed

Chasing a very simplistic modern design with a logo incorporating "TRV".
I'm starting a plumbing business.
I do water, sanitary and drainage plumbing that will cover residential, commercial, rental, rural, excavation, new housing and all maintanence requirements.

Industry/Entity Type

Business

Contact Information for Business Card

TRV PLUMBING SERVICES
DEAN HOLLOWBY - LICENSED PLUMBER
PHONE: 0481926574
E-MAIL: hollodt7@wirelane.com
NORTHERN SUBURBS

Requirements
Must have
• lower case email address

```html
<!DOCTYPE html>
<html lang="en">
<head>
<meta charset="utf-8">
<title>TRV Plumbing Services – Business Card</title>
<link rel="stylesheet" href="https://fonts.googleapis.com/css2?family=Archivo:ital,wght@0,400;0,700;0,800;0,900;1,300;1,400&display=swap">
<style>
  :root {
    --paper: #ffffff;
    --card-blue: #16a0dc;
    --card-orange: #f6931f;
    --ink: #2b2a29;
  }
  * { margin: 0; padding: 0; box-sizing: border-box; }
  html, body {
    width: 1200px;
    height: 900px;
    overflow: hidden;
    background: var(--paper);
  }
  body {
    position: relative;
    font-family: "Archivo", "Helvetica Neue", Arial, sans-serif;
    color: var(--ink);
  }
  .card {
    position: absolute;
    left: 310px;
    width: 580px;
    height: 340px;
  }
  .card--front {
    top: 59px;
    background: var(--card-blue);
  }
  .card--back {
    top: 499px;
    background: var(--card-orange);
  }

  /* Front: brand name */
  .brand {
    position: absolute;
    left: 0;
    right: 0;
    top: 149px;
    display: flex;
    flex-direction: column;
    align-items: center;
  }
  .brand__name {
    font-weight: 900;
    font-size: 100px;
    line-height: 1;
    letter-spacing: -2px;
    color: var(--ink);
  }
  .brand__trade {
    margin-top: -8px;
    font-weight: 900;
    font-size: 20px;
    letter-spacing: 0.2px;
    color: var(--ink);
  }

  /* Back: contact details */
  .holder {
    position: absolute;
    left: 37px;
    top: 32px;
  }
  .holder__name {
    font-weight: 900;
    font-size: 26px;
    line-height: 30px;
    letter-spacing: 0.3px;
  }
  .holder__role {
    font-style: italic;
    font-weight: 300;
    font-size: 23px;
    line-height: 28px;
  }
  .contact {
    position: absolute;
    left: 37px;
    top: 106px;
    display: grid;
    grid-template-columns: 177px auto;
    row-gap: 3px;
    font-size: 22px;
    line-height: 28px;
  }
  .contact__label { font-weight: 700; }
  .contact__value { font-weight: 400; }
  .area {
    position: absolute;
    left: 37px;
    top: 279px;
    font-style: italic;
    font-weight: 400;
    font-size: 22px;
    line-height: 28px;
  }
</style>
</head>
<body>
  <section class="card card--front" aria-label="Card front">
    <div class="brand">
      <span class="brand__name">TRV</span>
      <span class="brand__trade">PLUMBING SERVICES</span>
    </div>
  </section>

  <section class="card card--back" aria-label="Card back">
    <div class="holder">
      <p class="holder__name">DEAN HOLLOWBY</p>
      <p class="holder__role">LICENSED PLUMBER</p>
    </div>
    <div class="contact">
      <span class="contact__label">PHONE:</span>
      <span class="contact__value">0481926574</span>
      <span class="contact__label">E-MAIL:</span>
      <span class="contact__value">hollodt7@wirelane.com</span>
    </div>
    <p class="area">NORTHERN SUBURBS</p>
  </section>
</body>
</html>
```